Finally a Vodka produced for women ! (Label Design)

We are a small distillery based in Melbourne, Australia and we need a Vodka label design solution that will appeal to women aged 30-50 years and radiate luxury. Full Details are in a design brief attached. We thank you in advance.

Target Market(s)

Affluent females 30-50 years.

Industry/Entity Type

Spirits/Alcohol

Requirements
Must have
• Be clear this is a luxury Vodka.
Nice to have
• Elegance.

```html
<!DOCTYPE html>
<html lang="en">
<head>
<meta charset="utf-8">
<title>Silver Wren Premium Vodka – Label Concepts</title>
<link rel="stylesheet" href="https://fonts.googleapis.com/css2?family=Cinzel:wght@400;500&family=Josefin+Sans:wght@600&family=Barlow+Condensed:wght@300;400&display=swap">
<style>
  :root {
    --pink: #ff88dc;
    --pink-soft: #f9b6e3;
    --ink: #1c1c1c;
    --white: #ffffff;
    --glass: #d9f1ee;
    --glass-edge: #8fc6e4;
    --outline: #a6a6a6;
    --note: #555555;
    --serif: "Cinzel", serif;
    --brand: "Josefin Sans", sans-serif;
    --cond: "Barlow Condensed", sans-serif;
  }
  * { margin: 0; padding: 0; box-sizing: border-box; }
  html, body { width: 1200px; height: 1044px; overflow: hidden; background: var(--white); }
  .board { position: relative; width: 1200px; height: 1044px; }

  /* ---------- bottle ---------- */
  .bottle { position: absolute; left: 0; top: 0; }
  .neck-strip {
    position: absolute; left: 317px; top: 142px; width: 61px; height: 151px;
    background: var(--pink);
    border-left: 2px solid var(--white); border-right: 2px solid var(--white);
  }
  .neck-strip__text {
    position: absolute; left: 50%; top: 50%;
    transform: translate(-50%, -50%) rotate(-90deg);
    font-family: var(--serif); color: var(--white); font-size: 13px;
    line-height: 14px; text-align: center; white-space: nowrap; letter-spacing: 0.5px;
  }
  .type-premium, .type-vodka {
    position: absolute; left: 0; width: 694px; text-align: center;
    font-family: var(--serif); color: var(--ink);
  }
  .type-premium { top: 596px; font-size: 20px; letter-spacing: 3px; }
  .type-vodka { top: 616px; font-size: 43px; letter-spacing: 2px; }
  .band-quartz {
    position: absolute; left: 163px; top: 744px; width: 369px; height: 18px;
    background: var(--pink); color: var(--white);
    font-family: var(--serif); font-size: 11.5px; letter-spacing: 0.8px;
    text-align: center; line-height: 18px;
  }
  .band-origin {
    position: absolute; left: 142px; top: 773px; width: 410px; height: 40px;
    background: var(--ink); color: var(--white);
    border-top: 2px solid var(--ink); box-shadow: 0 -3px 0 -1px var(--white) inset;
    font-family: var(--serif); font-size: 11.5px; letter-spacing: 0.6px;
  }
  .band-origin__left, .band-origin__right { position: absolute; top: 10px; }
  .band-origin__left { left: 24px; }
  .band-origin__right { right: 32px; }
  .band-origin__seal {
    position: absolute; left: 290px; top: 773px; width: 114px; height: 88px;
    background: var(--ink); border-radius: 0 0 57px 57px;
    border: 2px solid var(--white); border-top: none;
    box-shadow: 0 0 0 1px var(--ink);
  }
  .brand-name {
    position: absolute; left: 290px; top: 786px; width: 114px; text-align: center;
    font-family: var(--brand); font-weight: 600; color: var(--white);
  }
  .brand-name__main { font-size: 15px; letter-spacing: 3px; line-height: 18px; }
  .brand-name__sub { font-size: 6.5px; letter-spacing: 2.6px; margin-top: 3px; }
  .brand-name__rule { width: 26px; height: 1px; background: var(--white); margin: 8px auto 0; }
  .volume {
    position: absolute; left: 300px; top: 870px; width: 94px; text-align: center;
    font-family: var(--cond); font-weight: 400; color: #8a8a8a;
  }
  .volume__ml { font-size: 22px; line-height: 24px; border-bottom: 1px solid #8a8a8a; padding-bottom: 2px; }
  .volume__abv { font-size: 13px; margin-top: 3px; }

  /* ---------- strip concepts ---------- */
  .concept { position: absolute; left: 785px; width: 412px; height: 62px; }
  .concept__disc {
    position: absolute; left: 150px; top: -26px; width: 112px; height: 112px; border-radius: 50%;
  }
  .concept__band { position: absolute; inset: 0; }
  .concept__band::before, .concept__band::after {
    content: ""; position: absolute; left: 0; right: 0; height: 2.5px; background: currentColor;
  }
  .concept__band::before { top: 0; }
  .concept__band::after { bottom: 0; }
  .concept__fill { position: absolute; left: 0; right: 0; top: 5px; bottom: 5px; background: currentColor; }
  .concept__left, .concept__right, .concept__mark {
    position: absolute; color: var(--white); text-align: center;
  }
  .concept__left {
    left: 8px; width: 136px; top: 17px; font-family: var(--serif);
    font-size: 13.5px; line-height: 13px; letter-spacing: 0.6px;
  }
  .concept__right {
    left: 262px; width: 144px; top: 17px; font-family: var(--serif);
    font-size: 12.5px; line-height: 13px; letter-spacing: 0.8px;
  }
  .concept__mark {
    left: 150px; width: 112px; top: 24px; font-family: var(--serif);
    font-size: 10px; letter-spacing: 1px;
  }
  .is-black { color: var(--ink); }
  .is-pink { color: var(--pink); }
  .disc-pink { background: var(--pink); }
  .disc-black { background: var(--ink); }

  /* ---------- note ---------- */
  .note {
    position: absolute; left: 793px; top: 784px;
    font-family: var(--cond); font-weight: 300; color: var(--note); font-size: 14px;
  }
  .note__author { font-size: 13.5px; margin-bottom: 6px; }
  .note p { margin-left: 23px; line-height: 24.5px; }
  .note .gap { margin-top: 24px; }
</style>
</head>
<body>
<main class="board">

  <svg class="bottle" width="700" height="1044" viewBox="0 0 700 1044" role="img" aria-label="Faceted glass vodka bottle">
    <defs>
      <linearGradient id="glass" x1="0" y1="0" x2="0" y2="1">
        <stop offset="0" stop-color="#e6f5f4"/>
        <stop offset="1" stop-color="#cdeee8"/>
      </linearGradient>
      <radialGradient id="blush" cx="0.55" cy="0.4" r="0.6">
        <stop offset="0" stop-color="#f6a9dc" stop-opacity="0.9"/>
        <stop offset="1" stop-color="#f6a9dc" stop-opacity="0"/>
      </radialGradient>
    </defs>
    <!-- neck and cap -->
    <rect x="292" y="177" width="110" height="42" fill="#eef7f7" stroke="var(--outline)"/>
    <rect x="297" y="219" width="100" height="55" fill="#eef7f7" stroke="var(--outline)"/>
    <polygon points="297,274 397,274 420,299 274,299" fill="#eef7f7" stroke="var(--outline)"/>
    <rect x="291" y="142" width="112" height="33" rx="2" fill="var(--ink)" stroke="var(--outline)"/>
    <!-- body -->
    <polygon points="274,299 420,299 569,813 500,967 200,967 126,813"
             fill="url(#glass)" stroke="var(--glass-edge)" stroke-width="4"/>
    <polygon points="274,299 420,299 569,813 500,967 200,967 126,813"
             fill="none" stroke="var(--outline)" stroke-width="1.2"/>
    <line x1="274" y1="301" x2="420" y2="301" stroke="#2d6ca8" stroke-width="2"/>
    <polyline points="200,930 500,930" fill="none" stroke="var(--outline)" stroke-width="1.2"/>
    <polyline points="142,813 200,930 200,967 M552,813 500,930 500,967" fill="none" stroke="var(--outline)" stroke-width="1.2"/>
    <!-- soft watercolour wash -->
    <ellipse cx="350" cy="450" rx="120" ry="180" fill="url(#blush)" role="img" aria-label="Pink watercolour wash"/>
    <!-- faint crystal pattern area -->
    <rect x="190" y="570" width="320" height="330" fill="#ffffff" opacity="0.18" role="img" aria-label="Faint crystal facet pattern"/>
  </svg>

  <div class="neck-strip">
    <div class="neck-strip__text">ROSE QUARTZ<br>FILTERED</div>
  </div>

  <div class="type-premium">PREMIUM</div>
  <div class="type-vodka">VODKA</div>

  <div class="band-quartz">ROSE QUARTZ FILTERED</div>
  <div class="band-origin">
    <span class="band-origin__left">HANDCRAFTED</span>
    <span class="band-origin__right">IN AUSTRALIA</span>
  </div>
  <div class="band-origin__seal"></div>
  <div class="brand-name">
    <div class="brand-name__main">SILVER<br>WREN</div>
    <div class="brand-name__sub">DISTILLERY</div>
    <div class="brand-name__rule"></div>
  </div>

  <div class="volume">
    <div class="volume__ml">700ML</div>
    <div class="volume__abv">40% ALC/VOL</div>
  </div>

  <!-- neck strip concepts -->
  <section class="concept" style="top:174px">
    <div class="concept__disc disc-pink"></div>
    <div class="concept__band is-black"><div class="concept__fill"></div></div>
    <div class="concept__left">ROSE QUARTZ<br>FILTERED</div>
    <div class="concept__mark">SILVER WREN</div>
    <div class="concept__right">HANDCRAFTED<br>IN AUSTRALIA</div>
  </section>

  <section class="concept" style="top:332px">
    <div class="concept__disc disc-black"></div>
    <div class="concept__band is-pink"><div class="concept__fill"></div></div>
    <div class="concept__left">ROSE QUARTZ<br>FILTERED</div>
    <div class="concept__mark">SILVER WREN</div>
    <div class="concept__right">HANDCRAFTED<br>IN AUSTRALIA</div>
  </section>

  <section class="concept" style="top:491px">
    <div class="concept__disc disc-black"></div>
    <div class="concept__band is-black"><div class="concept__fill"></div></div>
    <div class="concept__left">ROSE QUARTZ<br>FILTERED</div>
    <div class="concept__mark">SILVER WREN</div>
    <div class="concept__right">HANDCRAFTED<br>IN AUSTRALIA</div>
  </section>

  <section class="concept" style="top:648px">
    <div class="concept__disc disc-pink"></div>
    <div class="concept__band is-pink"><div class="concept__fill"></div></div>
    <div class="concept__left">ROSE QUARTZ<br>FILTERED</div>
    <div class="concept__mark">SILVER WREN</div>
    <div class="concept__right">HANDCRAFTED<br>IN AUSTRALIA</div>
  </section>

  <aside class="note">
    <div class="note__author">LORCAN</div>
    <p>My preference is for the black lid and pink strip.</p>
    <p>The black lid balances out the black strip at the bottom of bottle.</p>
    <p class="gap">IMO Having same colour lid and strip defeats the purpose...</p>
    <p>it needs contrast to draw attention to the text.</p>
  </aside>

</main>
</body>
</html>
```